Meridel Nutrition needs Stationary and a business card

We would like to use our current logo. The text can be moved around as needed. The stationary needs to be a 'first page' where the logo is more prominent to be impressive on higher quality paper and a second page where the logo is more subtle where there will be much more information on the page. There are 2 clinic locations which will need include name, address, phone number, fax number, web address. The business card should be single sided and contain this information also.
The design must be contemporary and sophisticated as this is a science based diet run out of a medical clinic.

Target Market(s)

People wanting to lose weight, athletes looking to optimise performance, people with arthritis or fighting cancer

Industry/Entity Type

Business

Contact Information for Business Card

must use the logo. I have attached an example card with the practice details on it. there must be space for the doctors name. Also the website www.meridelnutrition.com.au

Requirements
Must have
• the logo, the business adresses and phone numbers, the website, the doctors name and qualifications
Nice to have
• some creativity
Should not have
• Do not simply reproduce the existing card please

```html
<!DOCTYPE html>
<html lang="en">
<head>
<meta charset="utf-8">
<title>Meridel Nutrition Stationery</title>
<link href="https://fonts.googleapis.com/css2?family=Mulish:wght@400;700;800&display=swap" rel="stylesheet">
<style>
:root{
  --bg:#cfd0d1;
  --paper:#ffffff;
  --card-back:#f1f2f3;
  --sky:#3bb9e8;
  --navy:#2c5f9b;
  --ink:#222222;
  --grey:#3a3a3a;
  --mist:#e3eef6;
}
*{margin:0;padding:0;box-sizing:border-box}
html,body{width:1200px;height:1200px;overflow:hidden;background:var(--bg);font-family:'Mulish',sans-serif}
.canvas{position:relative;width:1200px;height:1200px}
.sheet{position:absolute;background:var(--paper);box-shadow:0 2px 10px rgba(0,0,0,.12);overflow:hidden}
.letterhead{left:70px;top:204px;width:560px;height:792px}
.sheet svg.art{position:absolute;left:0;top:0}
.brand{position:absolute;display:flex;flex-direction:column;align-items:center;gap:8px}
.brand-dot{border-radius:50%;background:var(--sky)}
.brand-name{font-weight:800;color:var(--navy);letter-spacing:.02em;white-space:nowrap}
.letterhead .brand{left:26px;top:26px;width:120px}
.letterhead .brand-dot{width:66px;height:66px}
.letterhead .brand-name{font-size:12.5px}
.doctor{position:absolute;text-align:right}
.doctor .name{font-weight:800;color:var(--ink)}
.doctor .quals{color:var(--grey)}
.doctor .role{color:var(--sky)}
.letterhead .doctor{right:28px;top:48px}
.letterhead .doctor .name{font-size:13.5px}
.letterhead .doctor .quals{font-size:4.5px;margin-top:2px}
.letterhead .doctor .role{font-size:7.5px;margin-top:2px}
.watermark{position:absolute;left:150px;top:258px;width:280px;height:280px;border-radius:50%;background:var(--mist);opacity:.75}
.clinics{position:absolute;display:flex;line-height:1.3;white-space:nowrap}
.clinic{padding:0 8px}
.clinic.first{text-align:right;border-right:1px solid var(--sky)}
.clinic .loc{color:var(--sky)}
.letterhead .clinics{right:14px;top:668px;font-size:8.6px;color:var(--ink)}
.letterhead .clinic .gap{margin-top:5px}
.card{left:670px;width:460px;height:280px}
.card-front{top:290px}
.card-back{top:630px;background:var(--card-back)}
.card-front .brand{left:38px;top:44px;width:140px}
.card-front .brand-dot{width:96px;height:96px}
.card-front .brand-name{font-size:14px}
.card-front .doctor{right:24px;top:80px}
.card-front .doctor .name{font-size:12px;color:#fff}
.card-front .doctor .quals{font-size:4px;color:#fff}
.card-front .doctor .role{font-size:9px;color:#fff}
.card-front .clinics{right:16px;top:170px;font-size:8.4px;color:#fff}
.card-front .clinic.first{border-right-color:#fff}
.card-front .clinic .loc{color:#fff;font-weight:700}
.card-front .clinic .gap{margin-top:8px}
.card-back .brand{left:50%;top:62px;transform:translateX(-50%);width:200px}
.card-back .brand-dot{width:100px;height:100px}
.card-back .brand-name{font-size:17px}
</style>
</head>
<body>
<div class="canvas">

  <section class="sheet letterhead">
    <div class="watermark" role="img" aria-label="Faint large brand emblem watermark"></div>
    <svg class="art" width="560" height="792" viewBox="0 0 560 792" aria-hidden="true">
      <path d="M0,775 C100,730 220,725 330,755 C420,778 500,775 560,760 L560,792 L0,792Z" fill="var(--sky)"/>
      <path d="M0,744 C120,692 230,694 300,762 C220,718 120,716 0,762Z" fill="var(--navy)"/>
    </svg>
    <div class="brand"><span class="brand-dot"></span><span class="brand-name">MERIDEL NUTRITION</span></div>
    <div class="doctor">
      <div class="name">Dr Adrian Vell</div>
      <div class="quals">MBBS (NSW) MBiomedE FRACS (Ortho) FAOrthA</div>
      <div class="role">Orthopaedic Surgeon</div>
    </div>
    <div class="clinics">
      <div class="clinic first">
        <div class="loc">Ashbury Vale</div>
        <div>84 Calloway Street</div>
        <div>Ashbury Vale NSW 2040</div>
        <div>Tel: 02 9100 4821</div>
        <div class="gap">Knee Surgery</div>
        <div>www.valekneeclinic.com.au</div>
      </div>
      <div class="clinic">
        <div class="loc">Kestrel Park</div>
        <div>12-14 Linden Road</div>
        <div>Kestrel Park NSW 2139</div>
        <div>Tel: 02 9100 7365</div>
        <div class="gap">Shoulder and Elbow</div>
        <div>www.drvell.com.au</div>
      </div>
    </div>
  </section>

  <section class="sheet card card-front">
    <svg class="art" width="460" height="280" viewBox="0 0 460 280" aria-hidden="true">
      <path d="M364,0 L460,0 L460,280 L0,280 C150,262 232,200 272,120 C302,52 330,10 364,0Z" fill="var(--sky)"/>
      <path d="M0,278 C140,256 218,196 258,118 C292,50 322,8 356,0 C322,14 300,56 268,124 C226,206 148,262 0,280Z" fill="var(--navy)"/>
    </svg>
    <div class="brand"><span class="brand-dot"></span><span class="brand-name">MERIDEL NUTRITION</span></div>
    <div class="doctor">
      <div class="name">Dr Adrian Vell</div>
      <div class="quals">MBBS (NSW) MBiomedE FRACS (Ortho) FAOrthA</div>
      <div class="role">Orthopaedic Surgeon</div>
    </div>
    <div class="clinics">
      <div class="clinic first">
        <div class="loc">Ashbury Vale</div>
        <div>Knee Surgery</div>
        <div class="gap">84 Calloway Street</div>
        <div>Ashbury Vale NSW 2040</div>
        <div>02 9100 4821</div>
        <div>www.valekneeclinic.com.au</div>
      </div>
      <div class="clinic">
        <div class="loc">Kestrel Park</div>
        <div>Shoulder and Elbow</div>
        <div class="gap">12-14 Linden Road</div>
        <div>Kestrel Park NSW 2139</div>
        <div>02 9100 7365</div>
        <div>www.drvell.com.au</div>
      </div>
    </div>
  </section>

  <section class="sheet card card-back">
    <div class="brand"><span class="brand-dot"></span><span class="brand-name">MERIDEL NUTRITION</span></div>
  </section>

</div>
</body>
</html>
```